Business card design and logo needed - Photographer

I take photos of weddings, rodeos, snowmobiling.
Need a card to hand out to prospective clients.
Industry/Entity Type
Business
Contact Information for Business Card
Marcus Dolven Photography
Requirements
Must have
- Bold
Black or white base.
My website. www.MarcusDolven.example
Should not have
- camera/ lens/ aperture blades

```html
<!DOCTYPE html>
<html lang="en">
<head>
<meta charset="utf-8">
<title>Marcus Dolven Photography — Business Card</title>
<link rel="stylesheet" href="https://fonts.googleapis.com/css2?family=Bebas+Neue&display=swap">
<style>
  :root {
    --card-bg: #303030;
    --lime: #b8db4a;
  }
  html, body {
    margin: 0;
    padding: 0;
    width: 693px;
    height: 1200px;
    overflow: hidden;
    background: var(--card-bg);
  }
  .card {
    display: block;
    width: 693px;
    height: 1200px;
    background: var(--card-bg);
  }
  .card__text {
    font-family: "Bebas Neue", "Oswald", sans-serif;
    fill: var(--lime);
  }
  .card__name-first { font-size: 330px; }
  .card__name-last  { font-size: 338px; }
  .card__trade-top  { font-size: 243px; }
  .card__trade-bottom { font-size: 266px; }
  .card__website    { font-size: 110px; }
</style>
</head>
<body>
<svg class="card" viewBox="0 0 693 1200" xmlns="http://www.w3.org/2000/svg" role="img" aria-label="Marcus Dolven Photography business card">
  <rect width="693" height="1200" fill="var(--card-bg)"/>
  <text class="card__text card__name-first" x="51" y="333" textLength="592" lengthAdjust="spacingAndGlyphs">MARCUS</text>
  <text class="card__text card__name-last" x="90" y="593" textLength="559" lengthAdjust="spacingAndGlyphs">DOLVEN</text>
  <text class="card__text card__trade-top" x="85" y="796" textLength="558" lengthAdjust="spacing">PHOTO</text>
  <text class="card__text card__trade-bottom" x="51" y="993" textLength="592" lengthAdjust="spacingAndGlyphs">GRAPHY</text>
  <text class="card__text card__website" x="56" y="1093" textLength="582" lengthAdjust="spacingAndGlyphs">MARCUSDOLVEN.EXAMPLE</text>
</svg>
</body>
</html>
```